Ledgerline Systems Group business card design.

We are a software development company that develop Software for finance companies and related industries.

We need a 2 sided business card designed. We have a new logo already designed (see attached eps and ai) We are after a clean simple corporate look. One side with just our logo, and the second side with our details.

Marcus Thelwell
Managing Director

Suite 4 Level 9, 318 Harbin Lane Sydney NSW 2000

Direct: +61 2 9478 3062
Mobile: +61 4 1237 6845
Email: marcust@lsg.net.au
Web: www.lsg.net.au

I have included 2 logo files an .ai and .eps. I noticed that the lines either side of the partners looks a bit jaggered and needs to be made sharper.

I would like to introduce a little colour somewhere rather than having it all black and white. But not over the top, keeping with a simple clean corporate look. Perhaps a light blue on some of the text?

If you have other ideas would be pleased to review

Regards

Marcus T.

```html
<!DOCTYPE html>
<html lang="en">
<head>
<meta charset="utf-8">
<title>Ledgerline Systems Group – Business Card</title>
<link href="https://fonts.googleapis.com/css2?family=Open+Sans:wght@400;600;700&display=swap" rel="stylesheet">
<style>
  :root {
    --stage: #e9e9ec;
    --ink: #111111;
    --paper: #ffffff;
    --card-black: #0a0a0a;
    --brand-blue: #0a3fa6;
    --text-dark: #1a1a1a;
  }
  * { box-sizing: border-box; margin: 0; padding: 0; }
  html, body {
    width: 1200px; height: 900px; overflow: hidden;
    background: var(--stage);
    font-family: "Open Sans", Arial, sans-serif;
  }
  .stage {
    width: 1200px; height: 900px;
    display: flex; flex-direction: column; align-items: center; justify-content: center;
    gap: 40px;
  }
  .card {
    position: relative;
    width: 660px; height: 378px;
    box-shadow: 0 10px 28px rgba(0,0,0,.22);
    overflow: hidden;
  }
  /* Logo side */
  .card--back {
    background: var(--card-black);
    display: flex; align-items: center; justify-content: center;
  }
  .brand {
    display: flex; align-items: center; gap: 14px;
  }
  .brand__mark { width: 22px; height: 22px; background: currentColor; }
  .brand__name { font-weight: 700; letter-spacing: .02em; text-transform: uppercase; }
  .card--back .brand { color: var(--paper); }
  .card--back .brand__name { font-size: 30px; }

  /* Details side */
  .card--front { background: var(--paper); color: var(--text-dark); }
  .accent-bar { position: absolute; background: var(--brand-blue); height: 12px; }
  .accent-bar--top { top: 0; right: 0; width: 290px; }
  .accent-bar--bottom { bottom: 0; right: 0; width: 290px; height: 20px; }
  .rule { position: absolute; height: 2px; background: var(--brand-blue); }
  .rule--upper { left: 30px; right: 36px; top: 150px; }
  .rule--lower { left: 30px; right: 24px; top: 300px; }

  .card--front .brand { position: absolute; left: 36px; top: 72px; color: var(--ink); gap: 10px; }
  .card--front .brand__mark { width: 16px; height: 16px; }
  .card--front .brand__name { font-size: 17px; }

  .address {
    position: absolute; left: 372px; top: 62px;
    font-size: 14px; line-height: 1.35; font-weight: 400;
  }
  .person { position: absolute; left: 92px; top: 208px; text-align: center; }
  .person__name { color: var(--brand-blue); font-size: 21px; font-weight: 600; letter-spacing: .03em; text-transform: uppercase; line-height: 1.1; }
  .person__title { font-size: 14px; }

  .contacts { position: absolute; left: 400px; top: 166px; list-style: none; }
  .contacts li { display: flex; align-items: center; gap: 10px; font-size: 15px; line-height: 24px; }
  .contacts svg { width: 15px; height: 15px; fill: none; stroke: var(--brand-blue); stroke-width: 1.8; }
  .contacts .solid { fill: var(--brand-blue); stroke: none; }
</style>
</head>
<body>
<main class="stage">
  <section class="card card--back" aria-label="Business card, logo side">
    <div class="brand">
      <span class="brand__mark"></span>
      <span class="brand__name">Ledgerline Systems Group</span>
    </div>
  </section>

  <section class="card card--front" aria-label="Business card, details side">
    <span class="accent-bar accent-bar--top"></span>
    <span class="accent-bar accent-bar--bottom"></span>
    <span class="rule rule--upper"></span>
    <span class="rule rule--lower"></span>

    <div class="brand">
      <span class="brand__mark"></span>
      <span class="brand__name">Ledgerline Systems Group</span>
    </div>

    <address class="address" style="font-style:normal">
      Suite 4 Level 9, 318 Harbin Lane,<br>Sydney NSW 2000
    </address>

    <div class="person">
      <p class="person__name">Marcus Thelwell</p>
      <p class="person__title">Managing Director</p>
    </div>

    <ul class="contacts">
      <li>
        <svg viewBox="0 0 16 16"><path class="solid" d="M3 1.5l3 .5 1 3-2 1.3a8 8 0 0 0 4.7 4.7L11 9l3 1 .5 3-2 1.5C7 14 2 9 1.5 3.5z"/></svg>
        +61 2 9478 3062
      </li>
      <li>
        <svg viewBox="0 0 16 16"><rect x="4" y="1.5" width="8" height="13" rx="1.5"/><line x1="7" y1="12" x2="9" y2="12"/></svg>
        +61 4 1237 6845
      </li>
      <li>
        <svg viewBox="0 0 16 16"><rect class="solid" x="1" y="3" width="14" height="10" rx="1"/><path d="M1.5 3.8L8 9l6.5-5.2" stroke="#fff"/></svg>
        marcust@lsg.net.au
      </li>
      <li>
        <svg viewBox="0 0 16 16"><circle cx="8" cy="8" r="6.5"/><ellipse cx="8" cy="8" rx="3" ry="6.5"/><line x1="1.5" y1="8" x2="14.5" y2="8"/></svg>
        www.lsg.net.au
      </li>
    </ul>
  </section>
</main>
</body>
</html>
```